Brochure for medical doctor

I need a brochure for a medical doctor to promote his practice. The brochure should contain his picture, business information (use letterhead from attachment), and the following text:

- Now accepting PI cases on lien!
- Same and next business day appointments available for initial visits, pre-operative clearances, and all other medical needs

- Expedited medical reports sent quickly to your office

Medical

```html
<!DOCTYPE html>
<html lang="en">
<head>
<meta charset="utf-8">
<title>Medical Reports and Doctor's Lien – Flyer</title>
<link rel="stylesheet" href="https://fonts.googleapis.com/css2?family=Tinos:wght@400;700&family=Arimo:wght@400;700&display=swap">
<style>
  :root{
    --brand-blue:#2e2f92;
    --title-blue:#2a2c86;
    --brand-green:#12975a;
    --ink:#1d1d1d;
    --paper:#ffffff;
    --backdrop:#e4e4e4;
    --photo-light:#dfe6ee;
    --photo-mid:#b9c7d6;
  }
  *{margin:0;padding:0;box-sizing:border-box}
  html,body{width:1200px;height:900px;overflow:hidden;background:var(--backdrop)}
  .canvas{position:relative;width:1200px;height:900px}
  .flyer{position:absolute;left:296px;top:20px;width:607px;height:860px;background:var(--paper);overflow:hidden;box-shadow:0 4px 18px rgba(0,0,0,.18)}
  .abs{position:absolute}

  .header-shape{left:0;top:0}
  .title{left:29px;top:26px;width:293px;text-align:center;font-family:"Tinos",serif;font-weight:700;font-size:33px;line-height:34px;color:var(--title-blue);letter-spacing:.3px}
  .title .accent{color:var(--brand-green);font-weight:400}
  .title .plain{font-weight:400}

  .rule{height:0;border-top:1.5px dotted #333}
  .rule--top{left:27px;top:145px;width:302px}
  .rule--bottom{left:27px;top:277px;width:302px}

  .highlights{left:27px;top:158px;width:302px;list-style:none;font-family:"Tinos",serif;font-size:12.4px;line-height:13.5px;color:var(--ink)}
  .highlights li{position:relative;padding-left:23px;margin-bottom:11px;text-align:justify}
  .highlights li::before{content:"";position:absolute;left:2px;top:3px;width:9px;height:9px;border-radius:50%;background:var(--brand-green)}
  .highlights li.dot-blue::before{background:var(--brand-blue);top:10px}
  .highlights li.dot-blue{margin-bottom:12px}

  .green-bar{left:0;top:293px;width:330px;height:7px;background:var(--brand-green)}

  .portrait-ring{left:340px;top:24px;width:244px;height:244px;border-radius:50%;background:var(--paper);box-shadow:0 2px 6px rgba(0,0,0,.25)}
  .portrait-inner{left:10px;top:10px;width:224px;height:224px;border-radius:50%;border:4px solid var(--brand-blue);background:var(--paper);padding:4px}
  .portrait-photo{width:100%;height:100%;border-radius:50%;background:radial-gradient(circle at 55% 40%,var(--photo-light),var(--photo-mid) 70%,#8fa3b8)}

  .authorization{left:29px;top:333px;width:549px;font-family:"Arimo",sans-serif;font-size:8.6px;line-height:12.1px;color:var(--ink);text-align:justify}
  .assignment{left:29px;top:508px;width:549px;font-family:"Arimo",sans-serif;font-weight:400;font-size:11.2px;line-height:13.2px;color:#000;text-align:justify}

  .sign-label{font-family:"Tinos",serif;font-size:11px;color:var(--ink);letter-spacing:.2px;white-space:nowrap}
  .sign-patient-name{left:29px;top:566px}
  .sign-date{left:366px;top:566px}
  .sign-patient{left:29px;top:609px}
  .sign-guardian{left:366px;top:609px}
  .sign-blank{left:366px;top:589px;width:200px;border-top:1.5px dotted #333}

  .ack-band{left:0;top:640px;width:607px;height:37px;background:var(--brand-blue);color:#fff;font-family:"Tinos",serif;font-size:14.4px;letter-spacing:.3px;display:flex;align-items:center;justify-content:center}
  .ack-band strong{font-weight:700;margin-left:5px}

  .acknowledgement{left:29px;top:691px;width:549px;font-family:"Arimo",sans-serif;font-size:8.6px;line-height:12.1px;color:var(--ink);text-align:justify}

  .footer-shape{left:0;top:826px}
  .website{left:36px;top:832px;font-family:"Tinos",serif;font-size:13px;letter-spacing:3px;color:#fff}
</style>
</head>
<body>
<div class="canvas">
  <div class="flyer">
    <svg class="abs header-shape" width="607" height="312" viewBox="0 0 607 312" aria-hidden="true">
      <polygon points="466,0 607,0 607,310 310,310" fill="var(--brand-blue)"/>
    </svg>

    <h1 class="abs title">MEDICAL<br><span class="accent">REPORTS</span> <span class="plain">AND</span><br><span class="plain">DOCTOR’S</span> <span class="accent">LIEN</span></h1>

    <div class="abs rule rule--top"></div>
    <ul class="abs highlights">
      <li>Now accepting PI cases on lien!</li>
      <li class="dot-blue">Same and next business day appointments available for initial visits, pre-operative clearances, and all other medical needs</li>
      <li>Expedited medical reports sent quickly to your office</li>
    </ul>
    <div class="abs rule rule--bottom"></div>
    <div class="abs green-bar"></div>

    <div class="abs portrait-ring">
      <div class="abs portrait-inner">
        <div class="portrait-photo" role="img" aria-label="Portrait of the smiling doctor in a white coat with a stethoscope, clinic behind him"></div>
      </div>
    </div>

    <p class="abs authorization">I authorized the above doctor and or their authorized representatives to furnish my attorney, any attorney or attorneys who subsequently are either associated with the said attorney or substituted in their place, with a full report of my examination, diagnosis, treatment, prognosis, itemized bill of charges incurred, etc, in regard to the accident in which I was involved on ______________________, and hold the above doctor free and harmless from any liability in such transfer of information. ut of the proceeds of the settlement and/or judgment in my claim for personal injuries, I hereby assign, set over and transfer to the above doctor such monies due and owing to him or the group for medical, chiropractic. X-rays, physical therapy, supplies and or laboratory fees rendered to me, either by reason of the above accident or otherwise. I further give to the above doctor a lien on any and all fund received by me or in my behave in association with the settlement or satisfaction of judgement arising from claims presented on my behalf,I fully understand that I am directly responsible to said doctors/group for all medical bills submitted by them for services rendered to me. I further understand that such payment is not contingent on any settlement, judgement or verdict by which I may eventually receive said fee. In the event legal action shall be brought in order to enforce this lien, then the prevailing party shall be entitled to reasonable costs and attorney fees in addiction to any judgment rendered. It is acknowledged by the undersigned that this assignment and lien is further consideration for the services rendered by the above doctor in addition to the obligation to pay for the medical services.</p>

    <p class="abs assignment">Patient’s personal injury claim medical payments are hereby assigned and will be paid directly from the insurance company to Maplewood Medical Center. Attorney agrees to notify the doctors immediately of the name and contacting information of any attorney substituted in his or her place.</p>

    <span class="abs sign-label sign-patient-name">PRINT PATIENT NAME ...........................................</span>
    <span class="abs sign-label sign-date">DATE .....................................................</span>
    <div class="abs sign-blank"></div>
    <span class="abs sign-label sign-patient">SIGNATURE OF PATIENT .........................................</span>
    <span class="abs sign-label sign-guardian">SIGNATURE OF PARENT/GUARDIAN</span>

    <div class="abs ack-band">ACKNOWLEDGEMENT OF ASSIGNMENT AND <strong>LIEN BY ATTORNEY</strong></div>

    <p class="abs acknowledgement">The undersigned being the attorney of record on his own behalf and on behalf of any other attorney or attorneys who are associated with the undersigned or who are substituted in his stead for the above patient, does hereby acknowledge receipt of a copy of the assignment and lien, and said attorney acknowledges that he/she obligates themselves to the terms of the assignment and lien in consideration for the rendering of medical services to their client by the above doctor and rendering of a report and bill to said attorney. In the event legal section shall be brought in order to enforce this lien. Then the prevailing party shall be entitled to reasonable costs and attorney fees in addiction to any judgment rendered. A photographic reproduction of this authorization may be used in place of the original. No charges of alterations of the monies billed herein will be accepted unless confirmed in writing by the doctor. Please date, sign and return on copy as soon as possible to the above referenced medical provider of services in order that treatment can continue on the herein contained lien basis.</p>

    <svg class="abs footer-shape" width="607" height="34" viewBox="0 0 607 34" aria-hidden="true">
      <polygon points="350,20 607,20 607,34 350,34" fill="var(--brand-blue)"/>
      <polygon points="0,0 342,0 364,34 0,34" fill="var(--brand-green)"/>
    </svg>
    <span class="abs website">www.yourwebsite.com</span>
  </div>
</div>
</body>
</html>
```